Brantley Advisory Group provides support for renewable energy projects to utilities and suppliers

I need a professional looking business card that is both simple and elegant and unique. My clients are mostly large organizations not individuals. I am a consultant with my own company that is small but would like to give clients the impression I am larger. Smart grid, fiber optics, software, field hardware, distribution automation, substation automation, operations, energy storage/batteries, microgrids, customer service, strategy/roadmaps, conservation, Automated Metering Infrastruture (AMI or smart meters) are all areas of focus.

Target Market(s)

Utilities, suppliers, governmental agencies involved in energy. All types of energy especially natural gas and electrical. Especially renewable energy or green projects.

Contact Information for Business Card

Name - Mark Brantley Cell Phone - 425.318.2746 Email - mbrantley@brantleyag-example.com
Company - Brantley Advisory Group (logo) Title - Principal

Font styles to use
Serif
Sans Serif

Colors

Designer to choose colors to be used in the design.

Requirements
Must have
• Simple and professional and powerful.
• Unique/creative design.
Nice to have
• Utilize color scheme to accent logo colors. Maybe some geometric pattern on edge of card with color.
Should not have
• Busy, complicated, traditional

```html
<!DOCTYPE html>
<html lang="en">
<head>
<meta charset="utf-8">
<title>Brantley Advisory Group – Business Card</title>
<link rel="stylesheet" href="https://fonts.googleapis.com/css2?family=Montserrat:wght@400;500;700&display=swap">
<style>
  :root {
    --canvas-bg: #d9dadc;
    --brand-blue: #1d3f98;
    --brand-blue-deep: #17338a;
    --brand-green: #5a8f2e;
    --card-white: #f7f7f7;
    --divider: #a7a9ad;
    --text-blue: #1f3a8f;
  }
  * { box-sizing: border-box; margin: 0; padding: 0; }
  html, body {
    width: 1200px; height: 1021px; overflow: hidden;
    background: var(--canvas-bg);
    font-family: "Montserrat", "Helvetica Neue", Arial, sans-serif;
  }
  .canvas { position: relative; width: 1200px; height: 1021px; }

  .card {
    position: absolute;
    width: 700px; height: 400px;
    border-radius: 4px;
    box-shadow: 0 10px 28px rgba(0,0,0,0.22);
    overflow: hidden;
  }

  /* Back of card */
  .card-back { left: 360px; top: 60px; background: var(--brand-blue); }
  .card-back .pattern-area {
    position: absolute; inset: 0;
    background: linear-gradient(135deg, var(--brand-blue) 0%, var(--brand-blue-deep) 100%);
  }
  .card-back .wordmark {
    position: absolute; left: 84px; top: 210px;
    color: #ffffff; font-weight: 700; font-size: 34px; line-height: 1.15;
    letter-spacing: 0.5px;
  }
  .card-back .corner-square {
    position: absolute; right: 48px; bottom: 44px;
    width: 64px; height: 64px;
    border: 4px solid #ffffff; border-radius: 6px;
  }

  /* Front of card */
  .card-front { left: 140px; top: 520px; background: var(--card-white); }
  .brand-block {
    position: absolute; left: 40px; top: 156px;
    display: flex; align-items: center; gap: 14px;
  }
  .brand-block .brand-square {
    width: 40px; height: 40px;
    border: 4px solid var(--brand-blue); border-radius: 5px;
    flex: none;
  }
  .brand-block .wordmark {
    color: var(--brand-blue); font-weight: 700; font-size: 22px; line-height: 1.15;
  }
  .divider {
    position: absolute; left: 306px; top: 110px;
    width: 1px; height: 180px; background: var(--divider);
  }
  .contact {
    position: absolute; left: 336px; top: 120px; right: 40px;
    color: var(--text-blue);
  }
  .contact .person-name {
    font-weight: 700; font-size: 24px; letter-spacing: 0.5px; text-transform: uppercase;
  }
  .contact .person-title {
    color: var(--brand-green); font-size: 16px; font-weight: 500; margin-top: 2px;
  }
  .contact .details { list-style: none; margin-top: 16px; }
  .contact .details li {
    display: flex; align-items: center; gap: 9px;
    font-size: 14px; font-weight: 500; line-height: 26px;
    white-space: nowrap;
  }
  .contact .details svg { width: 15px; height: 15px; flex: none; }
</style>
</head>
<body>
<main class="canvas">

  <section class="card card-back" aria-label="Card back">
    <div class="pattern-area" role="img" aria-label="Subtle repeating geometric pattern in blue tones"></div>
    <p class="wordmark">Brantley<br>Advisory Group</p>
    <span class="corner-square" aria-hidden="true"></span>
  </section>

  <section class="card card-front" aria-label="Card front">
    <div class="brand-block">
      <span class="brand-square" aria-hidden="true"></span>
      <p class="wordmark">Brantley<br>Advisory Group</p>
    </div>

    <span class="divider" aria-hidden="true"></span>

    <div class="contact">
      <h1 class="person-name">Mark Brantley</h1>
      <p class="person-title">Principal</p>
      <ul class="details">
        <li>
          <svg viewBox="0 0 16 16" fill="none" stroke="#1f3a8f" stroke-width="1.4" aria-hidden="true">
            <rect x="4" y="1" width="8" height="14" rx="1.5"/>
            <line x1="7" y1="12.5" x2="9" y2="12.5"/>
          </svg>
          425.318.2746
        </li>
        <li>
          <svg viewBox="0 0 16 16" fill="none" stroke="#1f3a8f" stroke-width="1.4" aria-hidden="true">
            <rect x="1" y="3.5" width="14" height="9" rx="1"/>
            <polyline points="1,4 8,9.5 15,4"/>
          </svg>
          mbrantley@brantleyag-example.com
        </li>
        <li>
          <svg viewBox="0 0 16 16" fill="none" stroke="#5a8f2e" stroke-width="1.3" aria-hidden="true">
            <circle cx="8" cy="8" r="6.5"/>
            <ellipse cx="8" cy="8" rx="3" ry="6.5"/>
            <line x1="1.5" y1="8" x2="14.5" y2="8"/>
          </svg>
          www.brantleyag-example.com
        </li>
      </ul>
    </div>
  </section>

</main>
</body>
</html>
```